Upmarket Dessert Lounge needs a Business Card Design

We are an upmarket dessert lounge needing a business card to match our image.

We want something that is simple yet beautiful, feminine, classy, sophisticated and elegant. We want it to stand out and don't mind if it is bold.

The design should include our logo and colours of red or maroon with gold highlights. We don't mind if black is used.

Marlow & Quince

Target Market(s)

For those who like to indulge or treat themselves and give in to their temptations on good quality desserts.

Industry/Entity Type

Business

Requirements
Must have
• Must include our logo and our name

Marlow & Quince

M & Q

```html
<!DOCTYPE html>
<html lang="en">
<head>
<meta charset="utf-8">
<title>Marlow &amp; Quince — Business Card</title>
<link rel="stylesheet" href="https://fonts.googleapis.com/css2?family=Open+Sans:wght@400;600;700&display=swap">
<style>
  :root {
    --maroon: #7a1416;
    --peach: #ffd39b;
    --paper: #ffffff;
    --ink: #3b3b3b;
    --stage: #e4e4e4;
  }
  * { margin: 0; padding: 0; box-sizing: border-box; }
  html, body { width: 956px; height: 1200px; overflow: hidden; }
  body {
    position: relative;
    background: var(--stage);
    font-family: "Open Sans", Arial, sans-serif;
    color: var(--ink);
  }
  .card {
    position: absolute;
    left: 74px;
    width: 798px;
    height: 456px;
    border-radius: 28px;
    overflow: hidden;
  }
  .card--front { top: 97px; background: var(--paper); }
  .card--back { top: 632px; background: var(--peach); }

  .brand {
    position: absolute;
    left: 0; right: 0;
    display: flex;
    align-items: center;
    justify-content: center;
    color: var(--maroon);
    font-weight: 400;
    white-space: nowrap;
  }
  .brand-mark {
    display: block;
    background: var(--maroon);
    flex: none;
  }
  .card--front .brand { top: 90px; height: 60px; gap: 16px; font-size: 40px; letter-spacing: 1px; }
  .card--front .brand-mark { width: 22px; height: 22px; }
  .card--back .brand { top: 158px; height: 140px; gap: 30px; font-size: 104px; letter-spacing: 2px; }
  .card--back .brand-mark { width: 46px; height: 46px; }

  .name-band {
    position: absolute;
    top: 233px; left: 0;
    width: 684px; height: 54px;
    background: var(--peach);
    display: flex; align-items: center; justify-content: center;
    font-size: 23.5px;
    padding-left: 118px;
  }
  .name-band strong { font-weight: 700; }
  .name-band .designation { font-weight: 400; margin-left: 6px; }
  .accent-block {
    position: absolute;
    top: 233px; left: 694px;
    width: 104px; height: 54px;
    background: var(--maroon);
  }

  .contact-list {
    position: absolute;
    top: 302px; left: 126px;
    list-style: none;
    font-size: 18px;
    line-height: 28px;
  }
  .contact-list b { font-weight: 700; }
  .address {
    position: absolute;
    top: 387px; left: 433px;
    font-size: 19.5px;
    line-height: 27px;
    font-style: normal;
  }
</style>
</head>
<body>
  <section class="card card--front" aria-label="Business card front">
    <div class="brand"><span class="brand-mark"></span><span class="brand-name">Marlow &amp; Quince</span></div>
    <div class="name-band"><strong>Your Name -</strong><span class="designation">Designation</span></div>
    <div class="accent-block"></div>
    <ul class="contact-list">
      <li><b>p</b> : 123-456-7890</li>
      <li><b>c</b> : 123-456-7890</li>
      <li><b>f</b> : 123-456-7890</li>
      <li><b>e</b> : name@yourwebsite.com</li>
      <li><b>w</b> : www.marlowquince.com</li>
    </ul>
    <address class="address">0000, Street Name<br>City Name, Country Code.</address>
  </section>

  <section class="card card--back" aria-label="Business card back">
    <div class="brand"><span class="brand-mark"></span><span class="brand-name">M &amp; Q</span></div>
  </section>
</body>
</html>
```